KORBALT

The business want a professional looking business card. We have a scetch we will add but want the extra upgrade, and would like more suggestions for variations of our business cards.

```html
<!DOCTYPE html>
<html lang="en">
<head>
<meta charset="utf-8">
<title>KORBALT business cards</title>
<link href="https://fonts.googleapis.com/css2?family=Cinzel:wght@600&family=Mulish:wght@400&display=swap" rel="stylesheet">
<style>
  :root {
    --backdrop: #e4e4e4;
    --card-white: #ffffff;
    --gold-pale: #f7e49c;
    --gold-mid: #c9a45a;
    --gold-deep: #7c5523;
    --gold-warm: #b48a45;
    --gold-ink: #a87d2c;
    --gold-mark: #ecc96a;
  }
  * { margin: 0; padding: 0; box-sizing: border-box; }
  html, body {
    width: 1200px;
    height: 745px;
    overflow: hidden;
    background: var(--backdrop);
  }
  .canvas {
    position: relative;
    width: 1200px;
    height: 745px;
  }
  .card {
    position: absolute;
    width: 530px;
    height: 303px;
    border-radius: 2px;
  }
  .card--front {
    left: 45px;
    top: 120px;
    background: linear-gradient(100deg, var(--gold-pale) 0%, var(--gold-mid) 30%, var(--gold-deep) 62%, var(--gold-warm) 100%);
    display: flex;
    align-items: center;
    justify-content: center;
  }
  .brand {
    display: flex;
    align-items: center;
    gap: 12px;
    font-family: "Cinzel", serif;
    font-weight: 600;
    letter-spacing: 2px;
  }
  .brand__dot {
    width: 14px;
    height: 14px;
    border-radius: 50%;
  }
  .card--front .brand { color: var(--gold-mark); font-size: 40px; }
  .card--front .brand__dot { background: var(--gold-mark); }

  .card--back {
    left: 625px;
    top: 320px;
    background: var(--card-white);
    color: var(--gold-ink);
  }
  .holder {
    position: absolute;
    left: 38px;
    top: 42px;
  }
  .holder__company {
    font-family: "Cinzel", serif;
    font-weight: 600;
    font-size: 24px;
    letter-spacing: 1px;
  }
  .holder__role {
    font-family: "Mulish", sans-serif;
    font-size: 25px;
    margin-top: 8px;
  }
  .holder__name {
    font-family: "Mulish", sans-serif;
    font-size: 14px;
    letter-spacing: 0.5px;
    margin-top: 2px;
  }
  .contacts {
    position: absolute;
    left: 38px;
    top: 190px;
    list-style: none;
    font-family: "Mulish", sans-serif;
    font-size: 16px;
  }
  .contacts__item {
    display: flex;
    align-items: center;
    gap: 12px;
    height: 27px;
  }
  .contacts__icon { width: 16px; height: 16px; flex: none; }
  .card--back .brand {
    position: absolute;
    right: 34px;
    top: 78px;
    font-size: 30px;
    color: var(--gold-ink);
  }
  .card--back .brand__dot { background: var(--gold-ink); }
</style>
</head>
<body>
<main class="canvas">
  <section class="card card--front" aria-label="Card front">
    <div class="brand"><span class="brand__dot"></span>KORBALT</div>
  </section>

  <section class="card card--back" aria-label="Card back">
    <div class="holder">
      <p class="holder__company">KORBALT MOLDVIK</p>
      <p class="holder__role">CEO &amp; Founder</p>
      <p class="holder__name">Lars Henrik Moldvik</p>
    </div>

    <ul class="contacts">
      <li class="contacts__item">
        <svg class="contacts__icon" viewBox="0 0 16 16" fill="none" stroke="currentColor" stroke-width="1.6"><rect x="4" y="1" width="8" height="14" rx="1.5"/><line x1="7" y1="12.5" x2="9" y2="12.5"/></svg>
        <span>004795551284</span>
      </li>
      <li class="contacts__item">
        <svg class="contacts__icon" viewBox="0 0 16 16" fill="currentColor"><path d="M1 4h14v9H1z M1.8 4.6 8 9.3l6.2-4.7" stroke="#fff" stroke-width="1"/></svg>
        <span>korbalt.llc@mailpost.cm</span>
      </li>
      <li class="contacts__item">
        <svg class="contacts__icon" viewBox="0 0 16 16" fill="none" stroke="currentColor" stroke-width="1.2"><circle cx="8" cy="8" r="6.5"/><ellipse cx="8" cy="8" rx="3" ry="6.5"/><line x1="1.5" y1="8" x2="14.5" y2="8"/></svg>
        <span>www.korbalt.llc</span>
      </li>
    </ul>

    <div class="brand"><span class="brand__dot"></span>KORBALT</div>
  </section>
</main>
</body>
</html>
```